Create a Valdossi-looking dashboard for our Quiet Harbor Speedometer that can look similar to my AI-generated dashboard attached, but with: 1) clear borders on all four sides, 2) is created in a way that we can modify the numbers weekly, say maybe you create the graphic that we can inset the excel spreadsheet numbers into, but ideally mixed with the Valdossi look black leather bubble design shown in the dashboard?; 3) uses the exact numbers shown in the attachment; 4) the speedometer on top should have four equal colors of red on left (-1), then yellow (0), then light green (1), then medium green (2); 5) the gauge on the top left should be the graphic that includes 0-100% bar that is currently 33%, and right below that a -20 to +20 bar with the arrow pointing to 11.9%, with color coding similar to the graphic; 6) replace the Valdossi logo in the middle with a similar shaped shield with blue background with the "T" logo with the eagle inside it, like attached

```html
<!DOCTYPE html>
<html lang="en">
<head>
<meta charset="utf-8">
<title>Quiet Harbor Speedometer</title>
<link rel="stylesheet" href="https://fonts.googleapis.com/css2?family=Cinzel:wght@700&family=Barlow+Semi+Condensed:wght@600;700&display=swap">
<style>
  :root {
    --bg: #000000;
    --leather: #b01828;
    --leather-dark: #6e0c15;
    --carbon: #1c1c1e;
    --carbon-dark: #0b0b0c;
    --chrome: #c9ccd1;
    --gold: #e9b55a;
    --gold-deep: #b07a26;
    --ink: #0a0a0a;
    --row-bull: #1ff01c;
    --row-bullish: #22e6c2;
    --row-bearish: #f2ec14;
    --row-bear: #f26b6b;
    --gauge-red: #c8161b;
    --gauge-yellow: #e6c612;
    --gauge-lightgreen: #4cc43a;
    --gauge-green: #1a8f2a;
    --teal: #38e0b0;
    --silver-text: #e6e8ea;
  }
  * { box-sizing: border-box; margin: 0; padding: 0; }
  html, body { width: 1200px; height: 774px; overflow: hidden; background: var(--bg); }
  .dashboard { position: relative; width: 1200px; height: 774px; background: var(--bg); font-family: "Barlow Semi Condensed", sans-serif; }
  .dashboard-art { position: absolute; inset: 0; }
  .gauge-label { position: absolute; transform: translate(-50%, -50%); font-weight: 700; color: var(--gold); line-height: 1; }
  .main-label { font-size: 32px; }
  .scale-label { font-size: 12px; color: #f0d9a8; }
  .readout { position: absolute; transform: translate(-50%, -50%); font-size: 30px; font-weight: 700; color: var(--silver-text); line-height: 1; letter-spacing: -0.5px; }
  .brand-name { position: absolute; left: 609px; top: 262px; transform: translate(-50%, -50%); font-size: 11px; font-weight: 700; letter-spacing: 1px; color: var(--gold); white-space: nowrap; }
  .title { position: absolute; left: 605px; top: 399px; transform: translate(-50%, -50%); font-family: "Cinzel", serif; font-weight: 700; font-size: 27px; color: var(--gold); white-space: nowrap; letter-spacing: 0.5px; }
  .trend-table { position: absolute; left: 219px; top: 446px; width: 781px; }
  .trend-head, .trend-row { display: grid; grid-template-columns: 258px 230px 1fr; }
  .trend-head { height: 36px; align-items: center; }
  .trend-head span { text-align: center; font-size: 20px; font-weight: 600; color: var(--gold); }
  .trend-row { height: 44px; align-items: center; font-size: 16px; font-weight: 700; color: var(--ink); }
  .trend-row span { height: 100%; display: flex; align-items: center; justify-content: center; border-left: 1.5px dashed rgba(0,0,0,0.55); }
  .trend-row span:first-child { justify-content: flex-start; padding-left: 47px; border-left: none; }
  .row-bull { background: var(--row-bull); }
  .row-bullish { background: var(--row-bullish); margin: 0 27px 0 16px; grid-template-columns: 242px 230px 1fr; }
  .row-bearish { background: var(--row-bearish); margin: 0 30px 0 20px; grid-template-columns: 238px 230px 1fr; border-top: 1.5px solid rgba(0,0,0,0.4); }
  .row-bear { background: var(--row-bear); margin: 0 36px 0 24px; grid-template-columns: 234px 230px 1fr; border-top: 1.5px solid rgba(0,0,0,0.4); border-radius: 0 0 16px 16px; }
  .row-bull span:first-child { padding-left: 47px; }
  .row-bullish span:first-child { padding-left: 31px; }
  .row-bearish span:first-child { padding-left: 27px; }
  .row-bear span:first-child { padding-left: 23px; }
  .row-bullish { border-top: 1.5px solid rgba(0,0,0,0.4); }
</style>
</head>
<body>
<div class="dashboard">
  <svg class="dashboard-art" width="1200" height="774" viewBox="0 0 1200 774" aria-hidden="true">
    <defs>
      <linearGradient id="leatherFill" x1="0" y1="0" x2="0" y2="1">
        <stop offset="0" stop-color="var(--leather)"/>
        <stop offset="1" stop-color="var(--leather-dark)"/>
      </linearGradient>
      <linearGradient id="carbonFill" x1="0" y1="0" x2="0" y2="1">
        <stop offset="0" stop-color="#2a2a2d"/>
        <stop offset="1" stop-color="var(--carbon-dark)"/>
      </linearGradient>
      <linearGradient id="chromeStroke" x1="0" y1="0" x2="0" y2="1">
        <stop offset="0" stop-color="#f4f5f7"/>
        <stop offset="0.5" stop-color="#6d7178"/>
        <stop offset="1" stop-color="#d9dce0"/>
      </linearGradient>
      <radialGradient id="faceShade" cx="0.5" cy="0.5" r="0.5">
        <stop offset="0" stop-color="#000" stop-opacity="0.7"/>
        <stop offset="0.55" stop-color="#000" stop-opacity="0.35"/>
        <stop offset="1" stop-color="#000" stop-opacity="0.05"/>
      </radialGradient>
      <radialGradient id="smallFace" cx="0.45" cy="0.4" r="0.6">
        <stop offset="0" stop-color="#3a3d40"/>
        <stop offset="1" stop-color="#0c0d0e"/>
      </radialGradient>
      <linearGradient id="goldFill" x1="0" y1="0" x2="1" y2="1">
        <stop offset="0" stop-color="#fbe39a"/>
        <stop offset="1" stop-color="var(--gold-deep)"/>
      </linearGradient>
      <linearGradient id="rangeArc" x1="0" y1="0" x2="1" y2="0">
        <stop offset="0" stop-color="#3ccf3a"/>
        <stop offset="0.5" stop-color="#f2e21a"/>
        <stop offset="0.8" stop-color="#f08a1a"/>
        <stop offset="1" stop-color="#d81e1e"/>
      </linearGradient>
      <radialGradient id="lampGlow" cx="0.5" cy="0.5" r="0.5">
        <stop offset="0" stop-color="#ff8a8a"/>
        <stop offset="0.5" stop-color="#e01818"/>
        <stop offset="1" stop-color="#e01818" stop-opacity="0"/>
      </radialGradient>
      <clipPath id="faceClip"><circle cx="609" cy="332" r="194"/></clipPath>
    </defs>

    <!-- leather cowl -->
    <path class="cowl" fill="url(#leatherFill)" d="M86 300 C90 250 140 205 250 180 L400 150 C440 142 470 118 500 108 C560 88 660 88 720 108 C750 118 780 142 820 150 L970 180 C1080 205 1112 255 1112 300 L1112 340 L86 340 Z"/>

    <!-- carbon upper panel -->
    <path class="upper-panel" fill="url(#carbonFill)" stroke="#3a3a3e" stroke-width="2" d="M95 455 C92 380 120 300 190 268 L330 225 C380 212 420 205 440 200 C470 140 535 112 609 112 C683 112 748 140 778 200 C800 205 840 212 890 225 L1030 268 C1095 300 1115 380 1110 455 Z"/>

    <!-- indicator lamps -->
    <circle cx="351" cy="252" r="12" fill="url(#lampGlow)"/>
    <circle cx="857" cy="252" r="12" fill="url(#lampGlow)"/>

    <!-- main gauge -->
    <circle cx="609" cy="332" r="218" fill="#121214" stroke="url(#chromeStroke)" stroke-width="6"/>
    <circle cx="609" cy="332" r="200" fill="none" stroke="#3b3d42" stroke-width="4"/>
    <g clip-path="url(#faceClip)">
      <path fill="var(--gauge-red)" d="M609 332 L442.7 428 A192 192 0 0 1 442.7 236 Z"/>
      <path fill="var(--gauge-yellow)" d="M609 332 L442.7 236 A192 192 0 0 1 609 140 Z"/>
      <path fill="var(--gauge-lightgreen)" d="M609 332 L609 140 A192 192 0 0 1 775.3 236 Z"/>
      <path fill="var(--gauge-green)" d="M609 332 L775.3 236 A192 192 0 0 1 775.3 428 Z"/>
      <circle cx="609" cy="332" r="194" fill="url(#faceShade)"/>
      <g fill="none" stroke-width="14" stroke-dasharray="2 7.005">
        <path stroke="#ff5a4a" d="M460 418 A172 172 0 0 1 460 246"/>
        <path stroke="#fff36a" d="M460 246 A172 172 0 0 1 609 160"/>
        <path stroke="#9dff7a" d="M609 160 A172 172 0 0 1 758 246"/>
        <path stroke="#4df060" d="M758 246 A172 172 0 0 1 758 418"/>
      </g>
    </g>
    <!-- brand mark -->
    <circle cx="609" cy="236" r="11" fill="#1d2d6b"/>

    <!-- needle and hub -->
    <path class="hub-dome" fill="#3a3c40" stroke="url(#chromeStroke)" stroke-width="3" d="M547 372 A62 62 0 0 1 671 372 Z"/>
    <polygon fill="url(#goldFill)" points="603,336 609,212 615,336" transform="rotate(43 609 332)"/>
    <circle cx="609" cy="332" r="16" fill="url(#goldFill)"/>

    <!-- left gauge -->
    <circle cx="258" cy="363" r="110" fill="#101012" stroke="url(#chromeStroke)" stroke-width="5"/>
    <circle cx="258" cy="363" r="96" fill="url(#smallFace)"/>
    <path fill="none" stroke="#1f5a4a" stroke-width="4" d="M219 430.5 A78 78 0 1 1 297 430.5"/>
    <path fill="none" stroke="var(--teal)" stroke-width="10" d="M219 430.5 A78 78 0 0 1 197.4 313.9"/>
    <circle cx="258" cy="363" r="56" fill="#18191b" stroke="#2c2e31" stroke-width="3"/>

    <!-- right gauge -->
    <circle cx="949" cy="367" r="110" fill="#101012" stroke="url(#chromeStroke)" stroke-width="5"/>
    <circle cx="949" cy="367" r="96" fill="url(#smallFace)"/>
    <path fill="none" stroke="url(#rangeArc)" stroke-width="12" d="M870.2 380.9 A80 80 0 1 1 1010.3 418.4"/>
    <circle cx="949" cy="367" r="56" fill="#18191b" stroke="#2c2e31" stroke-width="3"/>
    <polygon fill="#0a0a0a" stroke="#f2d21a" stroke-width="1.5" points="949,287 943,313 955,313"/>

    <!-- title band -->
    <path class="title-band" fill="url(#carbonFill)" stroke="url(#chromeStroke)" stroke-width="3" d="M300 392 Q609 350 918 392 L1141 455 L62 455 Z"/>

    <!-- lower leather body and tray -->
    <path class="lower-body" fill="url(#leatherFill)" d="M186 470 L1018 470 L1014 540 C1006 600 990 640 960 664 L250 664 C220 640 200 600 192 540 Z"/>
    <path class="lower-tray" fill="#141416" stroke="url(#chromeStroke)" stroke-width="3" d="M206 470 L1000 470 L996 540 C990 600 975 632 950 652 L262 652 C236 632 220 600 212 540 Z"/>
    <rect class="shelf" x="62" y="452" width="1079" height="26" rx="10" fill="#1a1a1c" stroke="url(#chromeStroke)" stroke-width="3"/>
  </svg>

  <div class="gauge-label main-label" style="left:461px;top:332px">-1</div>
  <div class="gauge-label main-label" style="left:531px;top:227px">0</div>
  <div class="gauge-label main-label" style="left:660px;top:225px">1</div>
  <div class="gauge-label main-label" style="left:747px;top:332px">2</div>

  <div class="brand-name">QUIET HARBOR</div>

  <div class="readout" style="left:256px;top:365px">33%</div>
  <div class="readout" style="left:948px;top:370px">11.9%</div>

  <div class="gauge-label scale-label" style="left:971px;top:279px">0</div>
  <div class="gauge-label scale-label" style="left:887px;top:303px">10</div>
  <div class="gauge-label scale-label" style="left:857px;top:362px">20</div>
  <div class="gauge-label scale-label" style="left:1035px;top:344px">-10</div>
  <div class="gauge-label scale-label" style="left:1023px;top:418px">-20</div>

  <div class="title">QUIET HARBOR SPEEDOMETER</div>

  <div class="trend-table">
    <div class="trend-head"><span>GEAR</span><span>CURRENT TREND</span><span>LAST TREND CHANGE</span></div>
    <div class="trend-row row-bull"><span>2 TURBO BOOST</span><span>BULL</span><span>FRIDAY, AUGUST 15,</span></div>
    <div class="trend-row row-bullish"><span>1 ACCELERATOR PEDAL</span><span>BULISH</span><span>2025</span></div>
    <div class="trend-row row-bearish"><span>0 BRAKES</span><span>BEARISH</span><span>-</span></div>
    <div class="trend-row row-bear"><span>-1 REVERSE</span><span>BEAR</span><span>-</span></div>
  </div>
</div>
</body>
</html>
```